Mobile Optometry needs descriptive brochure and business cards for patients

I need a brochure design and business cards for a new optometry service that brings full ocular examination, refraction, and spectacle dispensing to the patient in need.
I will mainly be working out of senior homes so it needs to be very legible NO SMALL PRINT, CLEAR, CONSCIENCE.
The final design needs to incorporate the logo and colouring that was just selected from a previous project. I will add this file as soon as I get the final changes back from the designer.

Here is what I would like in the broacher. I don't have a fax number, website address, email address set up yet but have room for this.

Note: I have attached the logo I selected for the company. I may not have attached the most detailed version but this will give you an idea of colouring and style. I will upload the proper image soon.

Routine eye examinations are crucial for early detection of diseases of the eye and effects of systemic conditions for everybody. As we age we are at higher risk of vision loss due to Glaucoma, Age-related Macular Degeneration, Diabetic or Hypertensive Retinopathy, Cataracts and many other diseases.

During your complete ocular visual assessment you will be screened for all conditions that may be affecting you as well as treat any issues you may be suffering from. Common treatable complaints: Dry eyes, Watery eyes, Burning, Itching, Difficulty reading small print, Reduced distance vision, Glare, Light sensitiveness, and difficulty performing hobbies.

Here is what your complete examination includes

Step 1: Appointment Request
-Call
-Email
-Phone
-Fax

Step 2: Welcome form
-Patient Name, DOB, Veltmore Care Plan number
-List current medications, allergies
-Current Visual difficulties
-Previous spectacle prescription (if available)

Step 3: Ocular Visual Assessment and Discussion of Results
-History & Symptoms
-Refraction
-Dilation and thorough ocular/retinal screening
-Spectacle or magnifier dispense if required
-Ophthalmologist or medical practitioner referral if required

Step 4: Dispense and Delivery
-Return to fit custom made glasses
-Demonstrate use low vision device
-Discuss any questions/treatments/referrals
Updates

I have just increased the budget. I am running out of time and want some good designs. I want a modern, clean and clear product. Please submit, points for originality.

Target Market(s)

The target audience is Professionals, managers, senior care facilities, families. I want something clean and easy to read. I want something modern but not trendy and something that appeals to the masses.

Industry/Entity Type

Medical

Font styles to use
Sans Serif

Requirements
Must have
• easy to read
bright
professional
Contact information on the last page
Nice to have
• order of services layer out nicely. Try a version with clearly defined steps. Step 1. Step 2. Step 3. Could be multiple broachers that are packaged together.
Should not have
• cartoony
serif fonts (please use font that is in logo)

```html
<!DOCTYPE html>
<html lang="en">
<head>
<meta charset="utf-8">
<title>ClearPath Eye Care – Brochure and Business Card Preview</title>
<link href="https://fonts.googleapis.com/css2?family=Jost:wght@300;400;500&display=swap" rel="stylesheet">
<style>
:root{
  --teal:#33b5a0;
  --blue:#35a3d8;
  --green:#7cbd2a;
  --ink:#3a3a3c;
  --body:#5c5c5e;
  --paper:#ffffff;
  --bg-light:#e6e6e6;
  --bg-dark:#7a7a7a;
}
*{margin:0;padding:0;box-sizing:border-box}
html,body{width:1200px;height:1200px;overflow:hidden}
body{
  position:relative;
  font-family:"Jost",sans-serif;
  font-weight:300;
  color:var(--body);
  background:radial-gradient(circle at 50% 45%,var(--bg-light) 0%,#b5b5b5 45%,var(--bg-dark) 100%);
}
.board-title{
  position:absolute;right:74px;top:40px;text-align:right;
  color:#fff;font-size:16px;line-height:20px;font-weight:300;
}
.panel{position:absolute;background:var(--paper);overflow:hidden}
.cover{left:74px;top:37px;width:526px;height:370px}
.spread{left:74px;top:414px;width:1052px;height:371px}
.cards{left:74px;top:793px;width:371px;height:370px}
.back{left:600px;top:793px;width:526px;height:370px}

/* brand name: one colour, one weight, one plain circle */
.brand-name{position:absolute;display:flex;align-items:center;justify-content:center;
  font-weight:400;color:var(--ink);white-space:nowrap}
.brand-dot{border-radius:50%;background:var(--ink);flex:none}

.cover .brand-name{left:0;right:0;top:172px;font-size:36px;line-height:44px;gap:12px}
.cover .brand-dot{width:14px;height:14px}

/* spread */
.decor{position:absolute;inset:0}
.rule{position:absolute;height:1px;background:var(--blue);width:58px}
.intro{position:absolute;left:143px;top:107px;width:236px;font-size:7.4px;line-height:12px;text-align:justify}
.intro p{text-indent:12px;margin-bottom:12px}
.lead{position:absolute;left:551px;top:103px;width:170px;color:var(--blue);font-size:13.5px;line-height:16px;font-weight:400}
.steps{position:absolute;left:773px;top:21px;width:270px;list-style:none}
.step{margin-bottom:10px}
.step-title{display:flex;align-items:center;gap:12px;color:var(--teal);font-size:10.5px;line-height:14px;font-weight:400}
.step-num{width:12px;height:12px;border-radius:50%;background:var(--teal);color:#fff;font-size:8px;line-height:12px;text-align:center;font-weight:500;flex:none}
.step-items{list-style:none;margin:11px 0 0 29px;font-size:7.4px;line-height:12px}
.step-items li::before{content:"· "}

/* business cards */
.card{position:absolute;left:60px;width:252px;height:140px;border-radius:10px;background:var(--paper);box-shadow:0 2px 10px rgba(0,0,0,.22);overflow:hidden}
.card-back{top:28px}
.card-front{top:200px}
.card-band{position:absolute;left:0;right:0;top:0;height:22px;background:var(--blue)}
.card-address{position:absolute;left:24px;top:56px;font-size:8.5px;line-height:12px;color:var(--body);font-style:normal}
.card-address::before{content:"";display:block;width:30px;height:1px;background:var(--blue);margin-bottom:6px}
.card-front .brand-name{left:0;right:0;top:58px;font-size:16px;line-height:22px;gap:6px}
.card-front .brand-dot{width:7px;height:7px}

/* back cover */
.back .brand-name{left:370px;width:150px;top:220px;font-size:14px;line-height:20px;gap:5px}
.back .brand-dot{width:6px;height:6px}
.contact{position:absolute;left:380px;width:130px;top:273px;text-align:center;font-size:8.2px;line-height:12px;color:var(--body);font-style:normal}
</style>
</head>
<body>

<div class="board-title">ClearPath Eye Care<br>Brochure and Business Card Preview</div>

<section class="panel cover">
  <div class="brand-name"><span class="brand-dot"></span>ClearPath Eye Care</div>
</section>

<section class="panel spread">
  <svg class="decor" width="1052" height="371" viewBox="0 0 1052 371" aria-hidden="true">
    <path d="M-10 100 Q90 60 160 -10" fill="none" stroke="var(--green)" stroke-width="26"/>
    <path d="M930 -10 Q980 40 1060 48" fill="none" stroke="var(--blue)" stroke-width="26"/>
    <circle cx="526" cy="616" r="295" fill="none" stroke="var(--teal)" stroke-width="30"/>
  </svg>

  <span class="rule" style="left:143px;top:91px"></span>
  <div class="intro">
    <p>Routine eye examinations are crucial for early detection of diseases of the eye and effects of systemic conditions for everybody. As we age we are at higher risk of vision loss due to Glaucoma, Age-related Macular Degeneration, Diabetic or Hypertensive Retinopathy, Cataracts and many other diseases.</p>
    <p>During your complete ocular visual assessment you will be screened for all conditions that may be affecting you as well as treat any issues you may be suffering from. Common treatable complaints: Dry eyes, Watery eyes, Burning, Itching, Difficulty reading small print, Reduced distance vision, Glare, Light sensitiveness, and difficulty performing hobbies.</p>
  </div>

  <span class="rule" style="left:551px;top:91px"></span>
  <h2 class="lead">In four steps to a perfect complete examination</h2>

  <ol class="steps">
    <li class="step">
      <div class="step-title"><span class="step-num">1</span>Appointment Request</div>
      <ul class="step-items"><li>Call</li><li>Email</li><li>Phone</li><li>Fax</li></ul>
    </li>
    <li class="step">
      <div class="step-title"><span class="step-num">2</span>Welcome form</div>
      <ul class="step-items">
        <li>Patient Name, DOB, Veltmore Care Plan number</li>
        <li>List current medications, allergies</li>
        <li>Current Visual difficulties</li>
        <li>Previous spectacle prescription (if available)</li>
      </ul>
    </li>
    <li class="step">
      <div class="step-title"><span class="step-num">3</span>Ocular Visual Assessment and Discussion of Results</div>
      <ul class="step-items">
        <li>History &amp; Symptoms</li>
        <li>Refraction, Dilation and thorough ocular/retinal screening</li>
        <li>Spectacle or magnifier dispense if required</li>
        <li>Ophthalmologist or medical practitioner referral if required</li>
      </ul>
    </li>
    <li class="step">
      <div class="step-title"><span class="step-num">4</span>Dispense and Delivery</div>
      <ul class="step-items">
        <li>Return to fit custom made glasses</li>
        <li>Demonstrate use low vision device</li>
        <li>Discuss any questions/treatments/referral</li>
      </ul>
    </li>
  </ol>
</section>

<section class="panel cards">
  <div class="card card-back">
    <div class="card-band"></div>
    <address class="card-address">ClearPath Eye Care<br>57 Maple Court<br>Harlow Falls, IL 60412<br>USA</address>
  </div>
  <div class="card card-front">
    <div class="brand-name"><span class="brand-dot"></span>ClearPath Eye Care</div>
  </div>
</section>

<section class="panel back">
  <div class="brand-name"><span class="brand-dot"></span>ClearPath Eye Care</div>
  <address class="contact">ClearPath Eye Care<br>57 Maple Court<br>Harlow Falls, IL 60412<br>USA</address>
</section>

</body>
</html>
```